" A Voltrana é uma empresa cuja especialidade é atuar diretamente no setor de energia, oferecendo a seus clientes gestão de energia e utilidades (água, gás, vapor, ar comprimido) com o objetivo principal de obter informações, padrões e variáveis de consumo e também eficiência energética para agir de forma assertiva no foco do desperdício e na otimização da utilização dos recursos em um parque industrial ou edifício. "

```html
<!DOCTYPE html>
<html lang="pt-BR">
<head>
<meta charset="utf-8">
<title>Voltrana – Pasta institucional</title>
<link href="https://fonts.googleapis.com/css2?family=Montserrat:wght@400;600;700&display=swap" rel="stylesheet">
<style>
  :root {
    --bg: #e6e6e6;
    --green: #2f9a3a;
    --green-dark: #278a32;
    --orange: #f2a516;
    --white: #ffffff;
    --text-light: #d9efd9;
  }
  * { margin: 0; padding: 0; box-sizing: border-box; }
  html, body { width: 1200px; height: 1200px; overflow: hidden; }
  body {
    background: var(--bg);
    font-family: "Montserrat", sans-serif;
    position: relative;
  }
  .folder-back {
    position: absolute;
    left: 41px; top: 41px;
    width: 564px; height: 746px;
    background: var(--green);
  }
  .back-brand {
    position: absolute;
    left: 74px; top: 586px;
    display: flex; align-items: center; gap: 10px;
  }
  .brand-dot {
    width: 22px; height: 22px; border-radius: 50%;
    background: var(--white);
  }
  .back-brand .brand-name {
    font-weight: 700; font-size: 26px; color: var(--white);
    letter-spacing: 1px;
  }
  .back-contact {
    position: absolute;
    left: 74px; top: 634px;
    font-size: 10.5px; line-height: 18px;
    color: var(--text-light);
    list-style: none;
  }
  .folder-cover {
    position: absolute;
    left: 605px; top: 41px;
    width: 552px; height: 746px;
    background: var(--white);
  }
  .cover-stripe {
    position: absolute;
    left: 0; bottom: 0;
    width: 100%; height: 10px;
    background: var(--orange);
  }
  .cover-brand {
    position: absolute;
    left: 0; top: 140px; width: 100%;
    text-align: center;
  }
  .cover-brand .brand-row {
    display: inline-flex; align-items: center; gap: 10px;
  }
  .cover-brand .brand-dot { background: var(--orange); width: 26px; height: 26px; }
  .cover-brand .brand-name {
    font-weight: 700; font-size: 32px; color: var(--orange);
    letter-spacing: 1px;
  }
  .cover-brand .brand-tagline {
    margin-top: 4px;
    font-size: 13px; font-weight: 600; color: var(--green);
  }
  .folder-pocket {
    position: absolute;
    left: 24px; top: 763px;
    width: 580px; height: 410px;
  }
</style>
</head>
<body>
  <section class="folder-back">
    <div class="back-brand">
      <span class="brand-dot"></span>
      <span class="brand-name">VOLTRANA</span>
    </div>
    <ul class="back-contact">
      <li>VOLTRANA - Soluções em Energia</li>
      <li>CNPJ 00.000.000/0001-00</li>
      <li>Avenida Paulista Norte, 1200 - Edifício Aurora, 5º andar</li>
      <li>CEP 01310-000 - São Paulo/SP</li>
      <li>www.voltrana.com.br</li>
    </ul>
  </section>

  <section class="folder-cover">
    <div class="cover-brand">
      <div class="brand-row">
        <span class="brand-dot"></span>
        <span class="brand-name">VOLTRANA</span>
      </div>
      <p class="brand-tagline">Soluções em Energia</p>
    </div>
    <div class="cover-stripe"></div>
  </section>

  <svg class="folder-pocket" viewBox="0 0 580 410" aria-hidden="true">
    <path d="M0 0 L0 408 L452 408 Q490 408 530 360 Q576 306 576 260 L576 26 L50 26 Z" fill="var(--orange)"/>
  </svg>
</body>
</html>
```